Water Remediation & Restoration Industry

Our company is in need of a trifold design for the water remediation & restoration industry. This brochure's main purpose is to help our company advertise its services to our community as well as insurance company's, home owners, and building managers. We currently run a commercial cleaning company and this is a new branch of service that we offer. We would like for the colors to coordinate with the logo which are royal blue, grey and white. We would like for the brochure to incorporate photos showing thermal imaging, equipment such as fans, dehumidifiers etc, water floods/leaks. We are a QWSBT Certified firm and the details to include are the following:
Phone Number: 1-866-555-0183
Website: www.tplvworks.org
24 Hour Emergency Services
Emergency Mitigation
Water Extraction
Structural Drying
Dehumidication
Mold Remediation
Water Damage Restoration
Fire & Smoke Cleanup
Sewage & Toilet Overflows
Carpet & Upholstery Cleaning
Contents Cleaning
Monitoring/Coordination
Antimicrobial Application
Smoke & Odor Removal

```html
<!DOCTYPE html>
<html lang="en">
<head>
<meta charset="utf-8">
<title>TPLV Trifold Brochure</title>
<link href="https://fonts.googleapis.com/css2?family=Montserrat:ital,wght@0,400;0,500;0,600;0,700;0,800;1,700&display=swap" rel="stylesheet">
<style>
:root{
  --navy:#2f2b8c;
  --navy-dark:#221f6e;
  --grey:#8b8e93;
  --ink:#4a4a55;
  --paper:#ffffff;
  --stage:#d9dadc;
  --sky:#2c8fd0;
}
*{box-sizing:border-box;margin:0;padding:0}
html,body{width:1200px;height:2400px;overflow:hidden}
body{background:var(--stage);font-family:'Montserrat',sans-serif;color:var(--ink);position:relative}
.spread{position:absolute;left:50px;width:1100px;height:850px;background:var(--paper);box-shadow:0 10px 30px rgba(0,0,0,.18);overflow:hidden}
.spread.outside{top:140px}
.spread.inside{top:1320px}
.panel{position:absolute;top:0;width:366.67px;height:850px}
.panel.a{left:0}.panel.b{left:366.67px}.panel.c{left:733.33px}
.fold{position:absolute;top:0;width:1px;height:850px;background:rgba(0,0,0,.06)}
.abs{position:absolute}
svg.photo{position:absolute;display:block}
/* brand */
.brand{display:flex;align-items:center;gap:10px}
.brand-dot{width:34px;height:34px;border-radius:50%;background:var(--grey)}
.brand-name{font-weight:800;color:var(--navy);font-size:44px;letter-spacing:1px}
.brand-tag{font-weight:700;color:var(--navy);font-size:13px;margin-top:6px}
.brand.small .brand-dot{width:18px;height:18px}
.brand.small .brand-name{font-size:24px}
.brand.small+.brand-tag{font-size:8px;margin-top:3px}
/* outside A */
.reasons-title{font-weight:700;font-style:italic;color:var(--navy);font-size:15px;line-height:1.25;text-transform:uppercase}
.reason{margin-top:14px;font-size:9.5px;line-height:1.45;font-style:italic;padding-bottom:10px;border-bottom:1px solid var(--navy)}
.reason:last-child{border-bottom:none}
.reason b{display:block;color:var(--navy);font-size:12px;font-style:normal;margin-bottom:3px}
.badge{width:86px;height:86px;border-radius:10px;background:#222}
/* contact */
.contact-icons{display:flex;align-items:center;justify-content:center}
.contact-icons .ic{width:26px;height:26px;border-radius:50%;background:var(--navy);display:flex;align-items:center;justify-content:center}
.contact-icons .line{width:50px;height:2px;background:var(--navy)}
.contact{text-align:center;font-size:13px;line-height:1.5;color:#333}
/* cover */
.kicker{font-weight:500;letter-spacing:12px;font-size:18px;color:var(--ink);text-transform:uppercase}
.headline{font-weight:800;color:var(--navy);font-size:40px;line-height:1.02;text-transform:uppercase}
.phone-bar{background:var(--navy);color:#fff;font-weight:700;font-size:26px;display:flex;align-items:center;gap:14px;padding:8px 18px}
.web{font-weight:500;letter-spacing:4px;font-size:13px;color:var(--ink)}
/* inside */
.h2{font-weight:800;color:var(--navy);font-size:24px;line-height:1.05;text-transform:uppercase}
.body{font-size:10.5px;line-height:1.55;margin-top:10px}
.quote{font-size:21px;line-height:1.3;color:var(--ink)}
.quote b{font-weight:700;color:var(--navy);text-transform:uppercase}
.services{list-style:none}
.services li{display:flex;align-items:center;gap:10px;height:37px;border-bottom:1px solid #bbb;font-size:11px;font-weight:600;text-transform:uppercase;color:var(--ink)}
.services .dot{width:22px;height:22px;border-radius:50%;border:2px solid var(--navy);flex:none;display:flex;align-items:center;justify-content:center}
.services .dot i{width:8px;height:8px;background:var(--navy);border-radius:2px}
.emergency{background:var(--navy);color:#fff;border-radius:40px;display:flex;align-items:center;gap:16px;padding:12px 22px}
.emergency .clock{width:48px;height:48px;border-radius:10px;background:#fff;display:flex;align-items:center;justify-content:center}
.emergency .big{font-size:32px;font-weight:400;line-height:1}
.emergency .sm{font-size:12px;font-weight:700;text-transform:uppercase}
.call{font-size:11px;text-transform:uppercase;color:var(--ink)}
.call b{display:block;font-size:20px;color:var(--navy);font-weight:700}
</style>
</head>
<body>

<svg width="0" height="0" style="position:absolute">
  <defs>
    <linearGradient id="g-team" x1="0" y1="0" x2="1" y2="1"><stop offset="0" stop-color="#e9e7e4"/><stop offset=".5" stop-color="#9fb8cf"/><stop offset="1" stop-color="#cfc9c1"/></linearGradient>
    <linearGradient id="g-people" x1="0" y1="0" x2="1" y2="0"><stop offset="0" stop-color="#d6a04a"/><stop offset="1" stop-color="#9a9a96"/></linearGradient>
    <linearGradient id="g-thermal" x1="0" y1="0" x2="1" y2="1"><stop offset="0" stop-color="#3b4048"/><stop offset=".6" stop-color="#7d8a99"/><stop offset="1" stop-color="#c9d3dd"/></linearGradient>
    <linearGradient id="g-supplies" x1="0" y1="0" x2="1" y2="1"><stop offset="0" stop-color="#f1c23a"/><stop offset="1" stop-color="#4aa6de"/></linearGradient>
    <linearGradient id="g-floor" x1="0" y1="0" x2="1" y2="0"><stop offset="0" stop-color="#d9d6d0"/><stop offset="1" stop-color="#ead66a"/></linearGradient>
    <linearGradient id="g-staff" x1="0" y1="0" x2="1" y2="1"><stop offset="0" stop-color="#2b3a6a"/><stop offset="1" stop-color="#e8dfa8"/></linearGradient>
  </defs>
</svg>

<!-- OUTSIDE SPREAD -->
<section class="spread outside">
  <div class="fold" style="left:366.67px"></div><div class="fold" style="left:733.33px"></div>

  <div class="panel a">
    <svg class="photo" style="left:0;top:0" width="367" height="250" viewBox="0 0 367 250">
      <path role="img" aria-label="Photo of two smiling team members" d="M0 0H367V150C330 210 250 225 150 220L0 215Z" fill="url(#g-people)"/>
      <path d="M0 212L150 217C250 222 330 205 367 145V170C330 225 250 240 150 234L0 228Z" fill="var(--navy)"/>
    </svg>
    <div class="abs" style="left:34px;top:262px;width:300px">
      <p class="reasons-title">We are not your typical cleaning company.<br>Here are 3 core reasons why<br>we are different:</p>
      <div class="reason"><b>001.</b>We focus on our cleaners so that they can focus on you. Finding the perfect cleaner can be a real challenge. TPLV spends a tremendous amount of time finding, training and retaining the best cleaners the industry has to offer.</div>
      <div class="reason"><b>002.</b>It's not just about cleaning, it's about communication. TPLV recognizes that doing a great job is more than just providing great cleaning. We leverage technology to provide our clients clear and consistent communication about the job we do.</div>
      <div class="reason"><b>003.</b>No cleaning company cares more about quality, and we can prove it. From the technology we use, to our quality inspections, we invest heavily in making sure that we are providing you the best possible cleaning services. Quality is at the heart of why we do everything we do.</div>
    </div>
    <div class="abs badge" style="left:250px;top:735px" role="img" aria-label="Certified firm badge"></div>
  </div>

  <div class="panel b">
    <div class="abs contact-icons" style="left:0;width:367px;top:40px">
      <span class="ic"><svg width="12" height="14" viewBox="0 0 12 14"><path d="M6 0a5 5 0 0 1 5 5c0 4-5 9-5 9S1 9 1 5a5 5 0 0 1 5-5z" fill="#fff"/><circle cx="6" cy="5" r="2" fill="var(--navy)"/></svg></span>
      <span class="line"></span>
      <span class="ic"><svg width="12" height="12" viewBox="0 0 24 24"><path d="M6.6 10.8a15 15 0 0 0 6.6 6.6l2.2-2.2c.3-.3.7-.4 1-.2 1.1.4 2.3.6 3.6.6.6 0 1 .4 1 1V20c0 .6-.4 1-1 1A17 17 0 0 1 3 4c0-.6.4-1 1-1h3.5c.6 0 1 .4 1 1 0 1.3.2 2.5.6 3.6.1.3 0 .7-.2 1z" fill="#fff"/></svg></span>
      <span class="line"></span>
      <span class="ic"><svg width="13" height="10" viewBox="0 0 13 10"><rect x=".5" y=".5" width="12" height="9" fill="#fff"/><path d="M.5 .5l6 5 6-5" stroke="var(--navy)" fill="none"/></svg></span>
    </div>
    <div class="abs contact" style="left:0;width:367px;top:88px">
      <p>27 Orchard Lane<br>Maple Ridge, Kentucky 40999</p>
      <p style="margin-top:16px">1-866-555-0183</p>
      <p style="margin-top:16px">info@tplvworks.org</p>
    </div>
    <div class="abs" style="left:110px;top:735px">
      <div class="brand small"><span class="brand-dot"></span><span class="brand-name">TPLV</span></div>
      <p class="brand-tag">Commerical Cleaning &amp; Restoration</p>
    </div>
  </div>

  <svg class="photo" style="left:380px;top:200px" width="705" height="460" viewBox="0 0 705 460">
    <path role="img" aria-label="Photo of a cleaning crew vacuuming and wiping desks in an office" d="M40 90C90 40 200 60 330 80C420 90 430 20 520 10C620 0 690 60 700 170V440C600 460 460 420 360 360C300 320 200 340 110 330C30 320 0 250 10 170C15 130 25 105 40 90Z" fill="url(#g-team)"/>
    <path d="M40 90C90 40 200 60 330 80C420 90 430 20 520 10C440 40 420 105 330 98C200 80 100 62 40 90Z" fill="var(--navy)"/>
    <path d="M700 170C720 300 690 400 620 455C660 380 675 290 700 170Z" fill="var(--navy)"/>
  </svg>

  <div class="panel c">
    <div class="abs" style="left:50px;top:40px">
      <div class="brand"><span class="brand-dot"></span><span class="brand-name">TPLV</span></div>
      <p class="brand-tag">Commerical Cleaning &amp; Restoration</p>
    </div>
    <p class="abs kicker" style="left:38px;top:670px">Commercial</p>
    <h1 class="abs headline" style="left:36px;top:696px">Cleaning &amp;<br>Restoration</h1>
    <div class="abs phone-bar" style="left:30px;top:786px;width:306px">
      <svg width="18" height="18" viewBox="0 0 24 24"><path d="M6.6 10.8a15 15 0 0 0 6.6 6.6l2.2-2.2c.3-.3.7-.4 1-.2 1.1.4 2.3.6 3.6.6.6 0 1 .4 1 1V20c0 .6-.4 1-1 1A17 17 0 0 1 3 4c0-.6.4-1 1-1h3.5c.6 0 1 .4 1 1 0 1.3.2 2.5.6 3.6.1.3 0 .7-.2 1z" fill="#fff"/></svg>
      1-866-555-0183
    </div>
    <p class="abs web" style="left:40px;top:832px">www.tplvworks.org</p>
  </div>
</section>

<!-- INSIDE SPREAD -->
<section class="spread inside">
  <div class="fold" style="left:366.67px"></div><div class="fold" style="left:733.33px"></div>

  <div class="panel a">
    <svg class="photo" style="left:0;top:0" width="367" height="350" viewBox="0 0 367 350">
      <path role="img" aria-label="Photo of a hand holding a thermal imaging camera" d="M0 0H367V120C330 200 300 260 160 300L0 320Z" fill="url(#g-thermal)"/>
      <path d="M0 310L160 292C290 255 330 195 367 110V140C340 220 300 280 160 310L0 330Z" fill="var(--navy)"/>
      <path d="M0 40C60 20 140 15 200 30C130 30 60 45 0 70Z" fill="var(--navy)"/>
    </svg>
    <div class="abs" style="left:36px;top:372px;width:305px">
      <h2 class="h2">Experience<br>High-Tech Efficiency</h2>
      <p class="body">Central Valley Building Care follows a technology-based service delivery process. In our company, employees communicate with each other using smartphone/tablet apps so that they can track every cleaning team's whereabouts.</p>
      <p class="body">This enables main office managers to efficiently monitor work progress in real time. With this high-tech infrastructure in place, our cleaners can be able to relay on-the-spot customer requests to us immediately. We can then issue instructions just as quickly to employees on site.</p>
      <p class="quote" style="margin-top:34px">We <b>inspect</b> our work, <b>communicate</b> with our clients, and <b>adjust</b> where needed in order to provide the best in class service for your facilities, clients, and staff.</p>
    </div>
  </div>

  <div class="panel b">
    <div class="abs" role="img" aria-label="Illustration of a bucket of cleaning supplies" style="left:120px;top:40px;width:130px;height:130px;border-radius:20px;background:linear-gradient(135deg,#f1c23a,#e05a7a 50%,#4aa6de)"></div>
    <h2 class="abs h2" style="left:36px;top:196px">The Services<br>We Offer</h2>
    <ul class="abs services" style="left:36px;top:262px;width:300px">
      <li><span class="dot"><i></i></span>Emergency Mitigation</li>
      <li><span class="dot"><i></i></span>Water Extraction</li>
      <li><span class="dot"><i></i></span>Structural Drying</li>
      <li><span class="dot"><i></i></span>Dehumidication</li>
      <li><span class="dot"><i></i></span>Mold Remediation</li>
      <li><span class="dot"><i></i></span>Water Damage Restoration</li>
      <li><span class="dot"><i></i></span>Fire &amp; Smoke Cleanup</li>
    </ul>
    <svg class="photo" style="left:0;top:600px" width="367" height="250" viewBox="0 0 367 250">
      <path role="img" aria-label="Photo of a wet floor being mopped beside a caution sign" d="M60 90C120 30 250 10 367 20V250H80C30 220 20 140 60 90Z" fill="url(#g-floor)"/>
      <path d="M60 90C120 30 250 10 367 20V0C250 -5 110 20 40 90C0 140 10 220 80 250H100C40 220 20 140 60 90Z" fill="var(--navy)"/>
    </svg>
  </div>

  <div class="panel c">
    <ul class="abs services" style="left:36px;top:36px;width:300px">
      <li><span class="dot"><i></i></span>Sewage &amp; Toilet Overflows</li>
      <li><span class="dot"><i></i></span>Carpet &amp; Upholstery Cleaning</li>
      <li><span class="dot"><i></i></span>Contents Cleaning</li>
      <li><span class="dot"><i></i></span>Monitoring/Coordination</li>
      <li><span class="dot"><i></i></span>Antimicrobial Application</li>
      <li><span class="dot"><i></i></span>Smoke &amp; Odor Removal</li>
    </ul>
    <div class="abs emergency" style="left:36px;top:300px;width:300px">
      <span class="clock"><svg width="30" height="30" viewBox="0 0 30 30"><circle cx="15" cy="15" r="12" fill="none" stroke="var(--navy)" stroke-width="3"/><path d="M15 8v7l5 3" stroke="var(--navy)" stroke-width="3" fill="none" stroke-linecap="round"/></svg></span>
      <span><span class="big">24 HOUR</span><br><span class="sm">Emergency Services</span></span>
    </div>
    <p class="abs call" style="left:150px;top:395px">Call us today<b>1-866-555-0183</b></p>
    <div class="abs" style="left:50px;top:455px">
      <div class="brand small"><span class="brand-dot"></span><span class="brand-name">TPLV</span></div>
      <p class="brand-tag">Commerical Cleaning &amp; Restoration</p>
    </div>
    <svg class="photo" style="left:-80px;top:530px" width="447" height="320" viewBox="0 0 447 320">
      <path role="img" aria-label="Photo of a smiling cleaning staff member at work" d="M120 60C200 40 320 30 447 20V320H0C20 220 60 80 120 60Z" fill="url(#g-staff)"/>
    </svg>
  </div>
</section>

</body>
</html>
```